Business Consulting Business Card

professional business card with basic information (1) First and Last name (2) email address, (3) phone number, (4) website.

```html
<!DOCTYPE html>
<html lang="en">
<head>
<meta charset="utf-8">
<title>Tide Harbor – Business Card</title>
<link rel="stylesheet" href="https://fonts.googleapis.com/css2?family=Montserrat:wght@500&family=Source+Sans+3:wght@400&display=swap">
<style>
  :root {
    --backdrop: #d6d6d6;
    --card: #ffffff;
    --navy: #062a3d;
    --teal: #4fbcc3;
    --map-tint: #f1f1f1;
    --white: #ffffff;
  }
  * { margin: 0; padding: 0; box-sizing: border-box; }
  html, body {
    width: 1200px; height: 1200px; overflow: hidden;
    background: var(--backdrop);
  }
  .canvas { position: relative; width: 1200px; height: 1200px; }
  .card {
    position: absolute; left: 240px; width: 712px; height: 432px;
    background: var(--card); border-radius: 19px; overflow: hidden;
    font-family: "Source Sans 3", "Myriad Pro", sans-serif; color: var(--navy);
  }
  .card--front { top: 106px; }
  .card--back { top: 674px; }
  .map-area {
    position: absolute; left: 0; top: 0; width: 100%; height: 190px;
    background: linear-gradient(180deg, var(--map-tint) 0%, var(--map-tint) 55%, rgba(241,241,241,0) 100%);
  }
  .brand { position: absolute; display: flex; align-items: center; }
  .brand__dot { border-radius: 50%; background: var(--teal); flex: none; }
  .brand__name {
    font-family: "Montserrat", sans-serif; font-weight: 500;
    color: var(--navy); white-space: nowrap;
  }
  .card--front .brand { left: 45px; top: 58px; }
  .card--front .brand__dot { width: 40px; height: 40px; margin-right: 16px; }
  .card--front .brand__name { font-size: 22px; letter-spacing: 5px; }
  .person { position: absolute; right: 40px; top: 50px; text-align: right; }
  .person__name { font-size: 29px; color: var(--teal); line-height: 30px; }
  .person__title { font-size: 20px; color: var(--navy); line-height: 24px; }
  .person-bar {
    position: absolute; left: 698px; top: 53px; width: 14px; height: 46px;
    background: var(--navy);
  }
  .contacts { position: absolute; left: 42px; top: 163px; list-style: none; }
  .contacts li {
    display: flex; align-items: center; height: 36px;
    font-size: 20px; color: var(--navy);
  }
  .contacts svg { width: 18px; height: 18px; margin-right: 12px; flex: none; }
  .contacts li:nth-child(4) { margin-top: 1px; }
  .front-bands { position: absolute; left: 0; top: 0; width: 712px; height: 432px; }
  .social { position: absolute; left: 503px; top: 351px; width: 150px; text-align: center; }
  .social__label { font-size: 10.5px; color: var(--white); letter-spacing: 0.1px; }
  .social__icons { display: flex; justify-content: center; gap: 15px; margin-top: 11px; }
  .social__icons span {
    width: 34px; height: 34px; border-radius: 50%;
    border: 2px solid var(--white);
  }
  .card--back .brand { left: 0; right: 0; top: 172px; justify-content: center; }
  .card--back .brand__dot { width: 70px; height: 70px; margin-right: 24px; }
  .card--back .brand__name { font-size: 34px; letter-spacing: 8px; }
  .back-band {
    position: absolute; left: 0; top: 374px; width: 100%; height: 37px;
    background: var(--navy); color: var(--white);
    font-size: 20px; letter-spacing: 0.6px; text-align: center; line-height: 36px;
  }
  .back-strip {
    position: absolute; left: 0; top: 411px; width: 100%; height: 21px;
    background: var(--teal);
  }
</style>
</head>
<body>
<main class="canvas">

  <section class="card card--front">
    <div class="map-area" role="img" aria-label="Faint world map background"></div>

    <div class="brand">
      <span class="brand__dot"></span>
      <span class="brand__name">TIDE HARBOR</span>
    </div>

    <div class="person">
      <p class="person__name">Daniel Reeve</p>
      <p class="person__title">CEO/Founder</p>
    </div>
    <div class="person-bar"></div>

    <ul class="contacts">
      <li>
        <svg viewBox="0 0 24 24" fill="var(--teal)"><path d="M6.6 10.8a15.1 15.1 0 0 0 6.6 6.6l2.2-2.2c.3-.3.7-.4 1-.2 1.1.4 2.3.6 3.6.6.6 0 1 .4 1 1V20c0 .6-.4 1-1 1A17 17 0 0 1 3 4c0-.6.4-1 1-1h3.5c.6 0 1 .4 1 1 0 1.3.2 2.5.6 3.6.1.3 0 .7-.2 1z"/></svg>
        +014-555-0192
      </li>
      <li>
        <svg viewBox="0 0 24 24" fill="var(--teal)"><path d="M22 3 2 11l6 2.5L18 6l-8 8.5V21l3.5-4.5L18 19z"/></svg>
        info@tideharbor.com
      </li>
      <li>
        <svg viewBox="0 0 24 24" fill="none" stroke="var(--teal)" stroke-width="2"><circle cx="12" cy="12" r="9"/><path d="M3 12h18M12 3c3 3 3 15 0 18M12 3c-3 3-3 15 0 18"/></svg>
        www.tideharbor.com
      </li>
      <li>
        <svg viewBox="0 0 24 24" fill="var(--teal)"><path d="M12 2a7 7 0 0 0-7 7c0 5 7 13 7 13s7-8 7-13a7 7 0 0 0-7-7zm0 9.5a2.5 2.5 0 1 1 0-5 2.5 2.5 0 0 1 0 5z"/></svg>
        Address, Suit, City, Country, Zip
      </li>
    </ul>

    <svg class="front-bands" viewBox="0 0 712 432" aria-hidden="true">
      <path fill="var(--teal)" d="M0 369 H392 C408 369 418 358 426 347 C436 333 448 325 470 325 H712 V432 H0 Z"/>
      <path fill="var(--navy)" d="M0 347 H426 C418 358 408 369 392 369 H0 Z"/>
    </svg>

    <div class="social">
      <p class="social__label">FIND US ON SOCIAL MEDIA</p>
      <div class="social__icons">
        <span></span><span></span><span></span>
      </div>
    </div>
  </section>

  <section class="card card--back">
    <div class="map-area" role="img" aria-label="Faint world map background"></div>
    <div class="brand">
      <span class="brand__dot"></span>
      <span class="brand__name">TIDE HARBOR</span>
    </div>
    <div class="back-band">www.tideharbor.com</div>
    <div class="back-strip"></div>
  </section>

</main>
</body>
</html>
```